Brochure for Community-Based Therapy Company

Will be given out to patients, doctors, case managers. We are redesigning our marketing materials and would like a design for a brochure. We provide therapy to individuals who have been injured in car accidents or on the job. We provide occupational therapy, speech therapy and psychotherapy. We would like the brochure to utilize our corporate ID and color scheme that we are using for our other materials (see attached letterhead and logo).

Stock photos that are used should stay away from images of outpatient or hospital settings, stay away from photos with obvious disabilities (wheelchairs, learning to walk, etc), and nothing that looks like physical therapy, as we don't provide physical therapy only OT, Speech and psychotherapy. Would prefer to not have people wearing masks, as we will use this beyond the pandemic. Also, our staff wears business casual clothing so would prefer photos that the individuals are not wearing scrubs or other medical attire (lab coats, etc).

Target Market(s)

Patients, Physicians/Doctors, Case Managers

Industry/Entity Type

Healthcare

Requirements
Must have
• Prefer a booklet format but doesn't have to be 8.5 inch by 11 inch (can be a little smaller).

```html
<!DOCTYPE html>
<html lang="en">
<head>
<meta charset="utf-8">
<title>Therapy Services Brochure – Inner Spread</title>
<link href="https://fonts.googleapis.com/css2?family=Montserrat:wght@600;700&family=Open+Sans:ital,wght@0,400;0,600;1,400&display=swap" rel="stylesheet">
<style>
  :root{
    --backdrop:#3a3a3a;
    --paper:#ffffff;
    --sage-dark:#88a08f;
    --sage-mid:#b9cabd;
    --sage-light:#e3ebe5;
    --ink:#2f2f2f;
    --ink-soft:#4a4a4a;
    --photo-warm-a:#c9b59c;
    --photo-warm-b:#8f7a63;
    --photo-cool-a:#c8ccd0;
    --photo-cool-b:#7d848c;
  }
  *{box-sizing:border-box;margin:0;padding:0}
  html,body{width:1200px;height:833px;overflow:hidden}
  body{background:var(--backdrop);font-family:"Open Sans",Arial,sans-serif;color:var(--ink)}
  .spread{position:absolute;left:70px;top:36px;width:1060px;height:761px;display:flex;box-shadow:0 10px 30px rgba(0,0,0,.5)}
  .page{position:relative;width:530px;height:761px;background:var(--paper);padding:34px 34px 30px;overflow:hidden}
  .page--left{background:linear-gradient(to right,#fff 85%,#eeeeee)}
  .page--right{background:linear-gradient(to left,#fff 85%,#eeeeee)}
  .page::after{content:"";position:absolute;left:0;right:0;bottom:0;height:6px;background:var(--sage-mid)}

  .panel{background:linear-gradient(135deg,var(--sage-light),#eef2ef);border-radius:0 0 18px 0;position:relative}
  .panel__band{background:var(--sage-dark);color:#fff;font-family:"Montserrat",Arial,sans-serif;font-weight:700;font-size:11px;letter-spacing:.5px;padding:7px 18px;border-radius:0 16px 0 0}
  .panel__body{padding:12px 18px 16px}
  .columns{display:grid;grid-template-columns:1fr 1fr;gap:0 22px}

  .ticks{list-style:none}
  .ticks li{position:relative;padding-left:15px;font-size:8.4px;line-height:1.32;margin-bottom:6px;color:var(--ink-soft)}
  .ticks li::before{content:"";position:absolute;left:0;top:1px;width:8px;height:8px;border:1px solid var(--sage-dark);border-radius:50%}
  .ticks li::after{content:"";position:absolute;left:3px;top:3px;width:2px;height:3.5px;border:solid var(--sage-dark);border-width:0 1px 1px 0;transform:rotate(45deg)}
  .ticks--large li{font-size:10px;margin-bottom:3px;color:var(--ink)}

  .photo{display:block;width:100%;border-radius:0 0 16px 0}
  .photo--puzzle{height:220px;margin-top:-4px;background:linear-gradient(120deg,var(--photo-warm-a),var(--photo-warm-b) 55%,#e9e6e2 80%)}
  .photo--counsel{height:250px;margin-top:14px;border-radius:12px 0 16px 0;background:linear-gradient(110deg,#b9a99a,var(--photo-cool-a) 40%,var(--photo-cool-b) 75%,#d9d2cc)}

  .section-title{font-family:"Montserrat",Arial,sans-serif;font-weight:700;font-size:16px;letter-spacing:4px;text-transform:uppercase;color:var(--ink);padding-bottom:4px;border-bottom:1px solid var(--ink-soft);margin:22px 0 8px;display:inline-block}
  .intro{font-size:8.6px;line-height:1.4;color:var(--ink-soft);margin-bottom:10px}
  .panel--ot .panel__body{padding-top:10px}

  .right-list{margin-top:10px}
  .right-list li{margin-bottom:5px;font-size:8.6px}
  .panel--psych{border-radius:14px 0 18px 0;margin-top:4px}
  .panel--psych .panel__body{padding:14px 20px}
  .panel__lead{font-family:"Montserrat",Arial,sans-serif;font-weight:600;font-size:10.5px;line-height:1.35;color:var(--ink);margin-bottom:6px}
</style>
</head>
<body>
<main class="spread">
  <section class="page page--left">
    <div class="panel panel--speech">
      <div class="panel__band">SERVICES INCLUDE:</div>
      <div class="panel__body columns">
        <ul class="ticks">
          <li>Immediate and Short-Term Memory: compensatory strategies, modification of the environment for increased functional memory.</li>
          <li>Attention and concentration</li>
          <li>Expressive Language: ability to express ideas, verbally, or in written format, in a concise organized fashion.</li>
          <li>Comprehension and Retention of Verbal and Written Language</li>
          <li>Information Processing: gradually increase in the length and complexity of information presented to allow the brain to take in and process more information at one time.</li>
        </ul>
        <ul class="ticks">
          <li>Word Retrieval and Thought Formulation for Verbal and Written Expression</li>
          <li>Pragmatic Language/Social Communication</li>
          <li>Executive Functioning: The mental processes that enable individuals to plan, focus attention, retain instructions, and juggle multiple tasks successfully. Assist with planning, initiating, carrying out tasks, as well as assist with self-monitoring and awareness for carryover of strategies.</li>
          <li>Articulation</li>
          <li>Dysarthria (lack of voluntary control)</li>
          <li>Dysphagia (swallowing disorders)</li>
          <li>Voice</li>
        </ul>
      </div>
    </div>
    <div class="photo photo--puzzle" role="img" aria-label="Photo of two people's hands assembling a jigsaw puzzle on a table"></div>

    <h2 class="section-title">Occupational Therapy</h2>
    <p class="intro">Occupational Therapists are experts at the evaluation and analysis of an individual's abilities relative to the demands of an activity and use this perspective in order to determine any aspects of the person's life that have been impacted, including activities of daily living (i.e., self-care), instrumental activities of daily living (i.e., home management, rest and sleep habits, work demands, play, leisure, and social participation). Treatment includes re-learning how to do activities (remediation) or determining new ways of accomplishing them (compensatory strategies).</p>
    <div class="panel panel--ot">
      <div class="panel__band">SERVICES INCLUDE:</div>
      <div class="panel__body">
        <ul class="ticks">
          <li>Treatment of musculoskeletal (i.e., muscle strength, range of motion), sensory, perceptual, vestibular, and vascular, skin, or connective tissue impairments.</li>
          <li>Teach the use of memory compensation techniques such as daily planners, technological devices, checklists, and cueing systems</li>
        </ul>
      </div>
    </div>
  </section>

  <section class="page page--right">
    <ul class="ticks right-list">
      <li>Assist in developing effective schedules and routines</li>
      <li>Instruct individuals and family members in techniques to cope with behavioral changes and low frustration tolerance</li>
      <li>Assessment and treatment to maximize safety in the home and community environments.</li>
      <li>Recommendation of environmental adaptations to assist with physical, perceptual, and cognitive functioning, such as labeling cupboards and drawers, or using lighting to improve vision and/or attention to task</li>
      <li>Assist in re-learning social skills through techniques such as pre-processing and rehearsal, where the individual and therapist anticipate challenging social situations and practice appropriate responses</li>
      <li>Provide cognitive retraining exercises to address specific cognitive skills, such as attention, memory, and executive functioning</li>
      <li>Provide training and adaptation for activities of daily living, such as dressing, bathing, and grooming</li>
      <li>Provide training and assist in the development of compensatory techniques for instrumental activities of daily living, such as preparing meals, shopping, managing routine financial tasks, and caring for children</li>
      <li>Assist individuals with community re-integration, working with individuals in real life settings such as the grocery store, bank, mall, workplace, home, or any other environment in which individuals need to regain competence in occupational performance.</li>
      <li>Facilitate the identification and development of healthy, meaningful hobbies or other leisure activities</li>
      <li>Consult with employers and/or educational systems to adapt the work or school environment to facilitate the individual's performance abilities</li>
    </ul>

    <h2 class="section-title">Psychological and Counseling</h2>
    <div class="panel panel--psych">
      <div class="panel__body">
        <p class="panel__lead">Individual &amp; Family Counseling related to the injury<br>Psychological services are provided as needed and prescribed by the physician to:</p>
        <ul class="ticks ticks--large">
          <li>Address psychosocial needs of the patient.</li>
          <li>Address changes in family dynamics and other changes.</li>
          <li>Counsel the patient to ease symptoms of depression</li>
          <li>Assist with acceptance of change of life status, as a result of the injury.</li>
          <li>Provide the individual with coping strategies.</li>
        </ul>
      </div>
    </div>
    <div class="photo photo--counsel" role="img" aria-label="Photo of a couple talking with a counselor in a bright living room"></div>
  </section>
</main>
</body>
</html>
```